Employee Benefits Consulting Firm needs a refreshed website

I have a business (an employee benefits consulting firm) called KRV Benefits Group, LLC (www.krvbenefits-example.com).  The existing site is currently hosted on Nimbuspark.  The business has been pretty much dormant since 2012.  I've relaunched the business and need a new website and looking for the website to be in Wordpress and to start with just 5 pages:
Home
About Us
Services
Contact Us
Blog
Some information about KRV Benefits Group:
There is a tremendous waste (financial) in the traditional employee benefit model --- the current system is broken and simply stated, unsustainable. We take a very different approach when it comes to employee benefits consulting, constantly strive to provide short-term and long-term cost containment strategies that truly bend the healthcare cost curve... Many of our clients consider us as Benefit Architects...
Each employer/business is unique.
In short, our firm works with Employers to first understand their business.... -their history, their corporate structure, their leadership, their values, their uniqueness, etc.
Then we take a deep dive and get a strong grasp on their existing benefits program... -how did they get to where they are today, what are their goals/objectives, what is their risk tolerance, what are current pain points, are they compliant, etc.
Then after thorough analysis, we deliver a tailored solution. We implement the programs and manage the various aspects and moving parts of the program throughout the year.
We also are constantly analyzing the performance of the plan and monitor population health. We aggregate data and constantly refine the approach/strategy.

Updates
I made a few updates to the brief over the past couple of days...below is the updated brief:
Home
About Us
Services
Contact Us
Blog
MUST HAVE:
Mobile Friendly
PLEASE USE TORVEL THEME
SHOULD HAVE:
the ability to add embedded video client testimonials
the ability for online chat
SHOULD NOT HAVE:
Photos from the old/existing website, I apologize for the late directive

I apologize for the delay on responding. Content is just about complete and will submit ASAP. Please let me know your availability to complete this project.

Updated content has been posted to this project.  I appreciate everybody's patience as we are working through this!

Target Market(s)
This is a BtoB website, primarily focusing on the following targets: CFOs, CEOs, Directors of Human Resources
Industry/Entity Type
Consulting
Number of Pages Required
5+ page
Requirements
Must have
- Mobile Friendly
- PLEASE USE TORVEL THEME
Nice to have
- the ability to add embedded video client testimonials
- the ability for online chat
Should not have
- Photos from the old/existing website, I apologise for the late directive

```html
<!DOCTYPE html>
<html lang="en">
<head>
<meta charset="utf-8">
<title>KRV Benefits Group</title>
<link href="https://fonts.googleapis.com/css2?family=Open+Sans:wght@400;600;700&family=Raleway:wght@600;700;800&display=swap" rel="stylesheet">
<style>
:root{
  --blue:#1d87c9;
  --blue-dark:#12609a;
  --green:#8cc63f;
  --navy:#0c1a2b;
  --ink:#2a3340;
  --muted:#6c7580;
  --light:#eef1f4;
  --white:#ffffff;
}
*{box-sizing:border-box;margin:0;padding:0}
html,body{width:1200px;height:4412px;overflow:hidden}
body{font-family:"Open Sans",Arial,sans-serif;color:var(--ink);background:var(--white);position:relative}
section,header,footer{position:absolute;left:0;width:1200px;overflow:hidden}
.abs{position:absolute}
.title{font-family:"Raleway",Arial,sans-serif;font-weight:800;font-size:36px;text-align:center;color:var(--navy)}
.title span{color:var(--green)}
.title.light{color:var(--white)}
.btn{display:inline-block;background:var(--blue);color:var(--white);font-size:13px;font-weight:600;padding:9px 22px;border-radius:3px}
.para{font-size:12px;line-height:1.75;color:var(--muted)}
.photo{position:absolute}
.play{position:absolute;width:64px;height:64px;border-radius:50%;background:rgba(255,255,255,.9);left:50%;top:50%;margin:-32px 0 0 -32px}
.play::after{content:"";position:absolute;left:26px;top:20px;border-left:18px solid var(--blue);border-top:12px solid transparent;border-bottom:12px solid transparent}

/* header */
.site-header{top:0;height:48px;background:var(--white);box-shadow:0 1px 4px rgba(0,0,0,.1);z-index:5}
.brand{position:absolute;left:150px;top:13px;font-family:"Raleway",sans-serif;font-weight:700;font-size:17px;color:var(--blue);display:flex;align-items:center;gap:8px}
.brand i{width:18px;height:18px;background:var(--green);display:block}
.nav{position:absolute;left:500px;top:16px;display:flex;gap:34px;font-size:12px;font-weight:600;color:var(--ink)}
.nav .active{color:var(--green)}

/* hero */
.hero{top:48px;height:470px}
.hero-bg{left:0;top:0;width:1200px;height:470px;background:linear-gradient(120deg,#1d2a36,#3a4956 45%,#202c38)}
.hero-frame{left:252px;top:40px;width:500px;height:180px;border:2px solid rgba(255,255,255,.7)}
.hero h1{position:absolute;left:282px;top:62px;font-family:"Raleway",sans-serif;font-weight:800;font-size:42px;line-height:1.15;color:var(--white)}
.hero h1 span{color:var(--green)}
.hero .tag{position:absolute;left:282px;top:170px;font-size:17px;font-weight:600;color:var(--green)}
.hero .btn{position:absolute;left:282px;top:232px}
.dots{position:absolute;left:560px;top:300px;display:flex;gap:8px}
.dots i{width:10px;height:10px;border-radius:50%;background:rgba(255,255,255,.5);display:block}
.dots i.on{background:var(--white)}
.side-tab{right:0;top:130px;width:26px;height:120px;background:var(--white);border-radius:4px 0 0 4px}
.side-tab b{position:absolute;left:8px;top:20px;width:10px;height:80px;background:var(--green);border-radius:2px}

/* about */
.about{top:500px;height:570px}
.about .title{position:absolute;left:130px;top:10px;width:380px}
.about h3{position:absolute;left:130px;top:78px;width:380px;text-align:center;font-size:15px;color:var(--blue);font-weight:600}
.about .para{position:absolute;left:130px;top:112px;width:380px;text-align:center;font-size:11px}
.about .btn{position:absolute;left:278px;top:500px}
.about-photo{left:560px;top:0;width:460px;height:520px;background:linear-gradient(160deg,#dfe3e7,#c7ced5 60%,#eef0f2)}

/* services */
.services{top:1060px;height:630px}
.services-bg{left:0;top:0;width:1200px;height:630px;background:linear-gradient(180deg,#0f1d2d,#0a1421)}
.services .title{position:absolute;left:0;top:70px;width:1200px}
.services .intro{position:absolute;left:200px;top:135px;width:800px;text-align:center;color:#b9c3cd;font-size:11px;line-height:1.7}
.svc-photo{left:230px;top:275px;width:340px;height:250px;background:linear-gradient(135deg,#3c5468,#6d8294 50%,#2b3c4c)}
.svc-list{position:absolute;left:600px;top:280px;width:390px;color:#d5dde4}
.svc-list h4{font-size:13px;color:var(--white);font-weight:700;margin-bottom:10px}
.svc-list li{list-style:none;font-size:12px;line-height:2.05;padding-left:16px;position:relative}
.svc-list li::before{content:"";position:absolute;left:0;top:10px;width:7px;height:7px;background:var(--green)}
.svc-list .btn{margin-top:14px;margin-left:120px}

/* newsletter */
.newsletter{top:1690px;height:200px;background:var(--light)}
.newsletter .title{position:absolute;left:0;top:45px;width:1200px}
.sub-form{position:absolute;left:360px;top:112px;display:flex}
.sub-form .field{width:360px;height:36px;border:1px solid #c9d0d6;background:var(--white);font-size:11px;color:#9aa2aa;padding:11px 14px}
.sub-form .btn{border-radius:0;padding:10px 18px}

/* blog */
.blog{top:1890px;height:640px}
.blog-bg{left:0;top:0;width:1200px;height:640px;background:linear-gradient(180deg,#2a3038,#1b2026)}
.blog .title{position:absolute;left:0;top:40px;width:1200px}
.card{position:absolute;top:110px;width:240px;height:370px;background:rgba(20,26,33,.85)}
.card .img{position:absolute;left:0;top:0;width:240px;height:170px;background:linear-gradient(135deg,#5c6c7a,#8e9aa5)}
.card h5{position:absolute;left:12px;top:182px;width:216px;font-size:12px;color:var(--green);line-height:1.4}
.card p{position:absolute;left:12px;top:222px;width:216px;font-size:11px;color:#b5bec7;line-height:1.65}
.blog .btn{position:absolute;left:556px;top:512px}

/* team */
.team{top:2530px;height:410px}
.team .title{position:absolute;left:0;top:0;width:1200px}
.team-photo{left:230px;top:70px;width:340px;height:270px;background:linear-gradient(135deg,#3c6f96,#9db9cd)}
.member{position:absolute;left:610px;top:60px;width:370px;height:300px;box-shadow:0 2px 10px rgba(0,0,0,.15);background:var(--white)}
.avatar{position:absolute;left:155px;top:16px;width:60px;height:60px;border-radius:50%;background:linear-gradient(135deg,#b7c4cf,#7f8f9d)}
.member h4{position:absolute;top:84px;width:370px;text-align:center;font-size:13px;color:var(--blue)}
.member h6{position:absolute;top:102px;width:370px;text-align:center;font-size:11px;color:var(--ink);font-weight:600}
.member p{position:absolute;left:22px;top:126px;width:326px;font-size:10.5px;line-height:1.6;color:var(--muted)}
.member .btn{position:absolute;left:148px;top:252px;padding:7px 16px}

/* testimonial */
.testimonial{top:2940px;height:600px}
.testi-bg{left:0;top:0;width:1200px;height:600px;background:linear-gradient(180deg,#141a21,#0c1116)}
.testimonial .title{position:absolute;left:0;top:70px;width:1200px}
.laptop{left:440px;top:150px;width:320px;height:210px;background:linear-gradient(135deg,#2c5e85,#4f87b3);border:10px solid #20262c;border-radius:8px}
.laptop-base{position:absolute;left:400px;top:360px;width:400px;height:12px;background:#9aa3ab;border-radius:0 0 10px 10px}
.thumbs{position:absolute;left:400px;top:410px;display:flex;gap:12px;align-items:center}
.thumbs i{width:60px;height:50px;background:linear-gradient(135deg,#4b5966,#7c8995);display:block}
.thumbs i.on{outline:2px solid var(--green)}
.arrow{width:0;height:0;border-top:9px solid transparent;border-bottom:9px solid transparent}
.arrow.l{border-right:12px solid var(--white)}
.arrow.r{border-left:12px solid var(--white)}

/* contact */
.contact{top:3540px;height:640px}
.contact .title{position:absolute;left:0;top:20px;width:1200px}
.contact-info{position:absolute;left:230px;top:92px;width:340px;font-size:11px;color:var(--ink);line-height:1.8;display:grid;grid-template-columns:1fr 1fr}
.map{left:230px;top:150px;width:340px;height:300px;background:linear-gradient(135deg,#dfe6cf,#cfd9e2)}
.inquiry{position:absolute;left:620px;top:92px;width:350px}
.inquiry h4{font-family:"Raleway",sans-serif;font-size:16px;color:var(--blue);text-align:center;margin-bottom:12px}
.inquiry .f{height:28px;border:1px solid #cfd5db;margin-bottom:10px;font-size:10.5px;color:#959da5;padding:7px 10px}
.inquiry .f.area{height:80px}
.inquiry .btn{margin-left:122px;padding:7px 22px}

/* footer */
.site-footer{top:4180px;height:232px}
.footer-logo{position:absolute;left:560px;top:70px;width:80px;height:80px;border-radius:50%;background:var(--white);border:3px solid var(--green);display:flex;align-items:center;justify-content:center;font-family:"Raleway",sans-serif;font-weight:800;font-size:18px;color:var(--blue)}
.bottom-bar{position:absolute;left:0;top:196px;width:1200px;height:36px;background:var(--blue);color:var(--white);font-size:11px}
.bottom-bar span{position:absolute;left:150px;top:11px}
.social{position:absolute;right:150px;top:9px;display:flex;gap:10px}
.social i{width:18px;height:18px;border-radius:50%;background:rgba(255,255,255,.85);display:block}
</style>
</head>
<body>

<header class="site-header">
  <div class="brand"><i></i>KRV Benefits Group</div>
  <nav class="nav"><span class="active">Home</span><span>About Us</span><span>Services</span><span>Blog</span><span>Testimonials</span><span>Contact Us</span>
    <svg width="14" height="14" viewBox="0 0 14 14"><circle cx="6" cy="6" r="4.5" fill="none" stroke="#2a3340" stroke-width="1.6"/><line x1="9.5" y1="9.5" x2="13" y2="13" stroke="#2a3340" stroke-width="1.6"/></svg>
  </nav>
</header>

<section class="hero">
  <div class="photo hero-bg" role="img" aria-label="Dark photo of a business meeting with charts"></div>
  <div class="abs hero-frame"></div>
  <h1>Welcome To<br><span>KRV Benefits Group</span></h1>
  <div class="tag">The Benefit Of Innovative Thinking</div>
  <span class="btn">Consult Now</span>
  <div class="dots"><i></i><i class="on"></i><i></i></div>
  <div class="abs side-tab"><b></b></div>
  <svg class="abs" style="left:0;top:330px" width="1200" height="140" viewBox="0 0 1200 140" preserveAspectRatio="none">
    <path d="M0 80 Q600 150 1200 40 L1200 140 L0 140 Z" fill="#8cc63f"/>
    <path d="M0 100 Q600 160 1200 62 L1200 140 L0 140 Z" fill="#ffffff"/>
  </svg>
</section>

<section class="about">
  <div class="photo about-photo" role="img" aria-label="Street sign reading About KRV against a pale sky"></div>
  <h2 class="title">About <span>Us</span></h2>
  <h3>Employee Benefits Consulting</h3>
  <p class="para">The name KRV Benefits Group, LLC. At KRV Benefits Group we see a broken model in traditional employee benefits and we believe it can be fixed with a smarter approach. We work with employers to understand their history, their structure, their leadership and their values before we study any plan.<br><br>Our team of benefit architects looks closely at every existing program, how it came to be, what its goals are, the risk tolerance of the business and the pain points that drive cost year after year.<br><br>After careful analysis we deliver a tailored solution, implement each program and manage the moving parts through the year. We keep measuring plan performance and population health, aggregate the data and refine the strategy so that cost containment holds in the short and long term.</p>
  <span class="btn">Read More</span>
</section>

<section class="services">
  <div class="photo services-bg" role="img" aria-label="Dark navy backdrop"></div>
  <svg class="abs" style="left:0;top:0" width="1200" height="70" viewBox="0 0 1200 70" preserveAspectRatio="none"><path d="M0 0 L1200 0 L1200 20 Q600 80 0 20 Z" fill="#ffffff"/></svg>
  <h2 class="title light">Our <span>Services</span></h2>
  <p class="intro">Today employers face rising costs and tighter budgets, and the traditional benefit model has become hard to sustain. We partner with leadership teams to build strategies that control spending, bring clarity to every plan and keep employees well covered. Our approach blends data, advisory work and ongoing management so that programs stay compliant, transparent and stable. From plan design to renewal, we guide each step and measure results, helping employers reduce waste while giving their people benefits they value and trust every year.</p>
  <div class="photo svc-photo" role="img" aria-label="Photo of consultants reviewing documents at a desk"><span class="play"></span></div>
  <div class="svc-list">
    <h4>CONTROL, TRANSPARENCY, PLANNING, STABILITY</h4>
    <ul>
      <li>Benefit Innovation</li>
      <li>Reduce benefits costs while increasing value</li>
      <li>Challenging the Status Quo</li>
      <li>A Smarter Solution for Better Benefits – Value-Driven Benefits</li>
      <li>Expertise Where and When It Matters Most</li>
      <li>Innovative Thinking – Innovative Results</li>
      <li>Your Standards are High, Our Standard is Perfection</li>
      <li>Benefits custom tailored for your organization</li>
    </ul>
    <span class="btn">Read More</span>
  </div>
  <svg class="abs" style="left:0;top:560px" width="1200" height="70" viewBox="0 0 1200 70" preserveAspectRatio="none"><path d="M0 70 L0 40 Q600 -10 1200 40 L1200 70 Z" fill="#eef1f4"/></svg>
</section>

<section class="newsletter">
  <h2 class="title">Subscribe Our <span>Newsletter</span></h2>
  <div class="sub-form"><div class="field">Enter Your Email Address</div><span class="btn">Subscribe Now</span></div>
</section>

<section class="blog">
  <div class="photo blog-bg" role="img" aria-label="Darkened photo of an office team at work"></div>
  <svg class="abs" style="left:0;top:0" width="1200" height="40" viewBox="0 0 1200 40" preserveAspectRatio="none"><path d="M0 0 L1200 0 Q600 50 0 0 Z" fill="#eef1f4"/></svg>
  <h2 class="title light">Our <span>Blog</span></h2>
  <article class="card" style="left:220px"><div class="img" role="img" aria-label="Photo of a team meeting"></div><h5>Changing It Up With a New Plan Design</h5><p>Our team helps employers rethink plan design so that cost and coverage stay in balance. Small changes, guided by data, can lower spending while giving employees clearer choices and better access to care across the year.</p></article>
  <article class="card" style="left:480px"><div class="img" role="img" aria-label="Photo of colleagues around a table"></div><h5>Rising Health Costs And What Employers Can Do</h5><p>As costs rise each year, employers need a plan that goes beyond renewal. We review claims, compare options and build a long term strategy that keeps programs stable and affordable for everyone involved.</p></article>
  <article class="card" style="left:740px"><div class="img" role="img" aria-label="Photo of a presentation in a meeting room"></div><h5>Understanding The Value Of A Health Team</h5><p>A focused benefits team can give employers better insight into population health. By tracking results and refining programs, employers gain control and employees receive benefits that fit their needs.</p></article>
  <span class="btn">Read More</span>
  <svg class="abs" style="left:0;top:560px" width="1200" height="80" viewBox="0 0 1200 80" preserveAspectRatio="none"><path d="M0 80 L0 50 Q600 -10 1200 50 L1200 80 Z" fill="#ffffff"/></svg>
</section>

<section class="team">
  <h2 class="title">Our <span>Team</span></h2>
  <div class="photo team-photo" role="img" aria-label="Photo of a business group meeting"></div>
  <div class="member">
    <div class="avatar" role="img" aria-label="Portrait of the company president"></div>
    <h4>Daniel Marlowe CBC</h4>
    <h6>President</h6>
    <p>A graduate of the University of Lake Ridge, Daniel founded KRV Benefits Group with one goal: to help employers design benefit programs that make sense for their business and their people. With years of advisory experience he guides clients through plan design, funding, compliance and renewals, and leads the team in building long term strategies that reduce waste and support healthier employee populations.</p>
    <span class="btn">View All</span>
  </div>
</section>

<section class="testimonial">
  <div class="photo testi-bg" role="img" aria-label="Dark photo of a business audience"></div>
  <svg class="abs" style="left:0;top:0" width="1200" height="60" viewBox="0 0 1200 60" preserveAspectRatio="none"><path d="M0 0 L1200 0 L1200 10 Q600 80 0 10 Z" fill="#ffffff"/></svg>
  <h2 class="title light">Our <span>Testimonial</span></h2>
  <div class="photo laptop" role="img" aria-label="Video testimonial on a laptop screen"><span class="play"></span></div>
  <div class="laptop-base"></div>
  <div class="thumbs"><span class="arrow l"></span><i role="img" aria-label="Client video thumbnail"></i><i role="img" aria-label="Client video thumbnail"></i><i class="on" role="img" aria-label="Client video thumbnail"></i><i role="img" aria-label="Client video thumbnail"></i><i role="img" aria-label="Client video thumbnail"></i><span class="arrow r"></span></div>
  <svg class="abs" style="left:0;top:530px" width="1200" height="70" viewBox="0 0 1200 70" preserveAspectRatio="none"><path d="M0 70 L0 45 Q600 -15 1200 45 L1200 70 Z" fill="#ffffff"/></svg>
</section>

<section class="contact">
  <h2 class="title">Contact <span>Us</span></h2>
  <div class="contact-info"><span>2150 Harbor Point Drive, Lake Ridge, NY 10540</span><span>info@krvbenefits-example.com<br>(555) 014-2290</span></div>
  <div class="photo map" role="img" aria-label="Street map showing the office location"></div>
  <div class="inquiry">
    <h4>Get Your Inquiry</h4>
    <div class="f">Regarding</div>
    <div class="f">Name</div>
    <div class="f">Email Address</div>
    <div class="f">Company Name</div>
    <div class="f">Phone Number</div>
    <div class="f area">Please Share Your Needs</div>
    <span class="btn">Submit</span>
  </div>
</section>

<footer class="site-footer">
  <svg class="abs" style="left:0;top:90px" width="1200" height="110" viewBox="0 0 1200 110" preserveAspectRatio="none">
    <path d="M0 110 L0 70 Q600 -20 1200 70 L1200 110 Z" fill="#8cc63f"/>
    <path d="M0 110 L0 84 Q600 0 1200 84 L1200 110 Z" fill="#1d87c9"/>
  </svg>
  <div class="footer-logo">KRV</div>
  <div class="bottom-bar"><span>Copyright © KRV Benefits Group. All Rights Reserved.</span><div class="social"><i></i><i></i><i></i><i></i></div></div>
</footer>

</body>
</html>
```